Exercise Physiologist needs business cards

I have a logo, I need business cards (Sole trader) as I am moving to a new location and would like an updated look. I provide gym based exercise rehabilitation, injury prevention and movement assessments. I have over 13 years experience as an Exercise Physiologist. I would like the cards to look professional but not boring and can be a little different to stand out when sitting with other Allied Health Professional cards.

Target Market(s)

GP's, Allied health practitioners, people with injuries wanting to exercise

Industry/Entity Type

Health And Wellness

Contact Information for Business Card

Megan Dorrit - Exercise Physiologist 0437 582 906
14 Larkspur Bend Rd
Wexley South
(Gate 4, Brannock Fitness)
vantorahealth@maildrop-example.com
socialpage-example.com/Vantora

Requirements
Must have
• I would like to include a section to add next appointment date and time space to the back of the card.
Nice to have
• Rounded corners and a black background on 1 or 2 sides.
Should not have
• Pictures of fit/toned bodies etc

```html
<!DOCTYPE html>
<html lang="en">
<head>
<meta charset="utf-8">
<title>Vantora Health &amp; Rehabilitation – Business Card</title>
<link href="https://fonts.googleapis.com/css2?family=Roboto+Condensed:wght@400;700&display=swap" rel="stylesheet">
<style>
  :root {
    --backdrop: #8fcbd9;
    --card-white: #ffffff;
    --card-shade: #f1f1f1;
    --brand-navy: #1f4e96;
    --brand-sky: #4a9cd0;
    --brand-blue: #2457a4;
    --soft-panel: #edf3f9;
    --field-white: #ffffff;
  }
  * { margin: 0; padding: 0; box-sizing: border-box; }
  html, body {
    width: 1200px; height: 1200px; overflow: hidden;
    background: var(--backdrop);
    font-family: "Roboto Condensed", Arial, sans-serif;
  }
  .sheet {
    width: 1200px; height: 1200px;
    display: flex; flex-direction: column; align-items: center; justify-content: center;
    gap: 60px;
  }
  .card {
    position: relative;
    width: 840px; height: 513px;
    border-radius: 14px;
    overflow: hidden;
    box-shadow: 0 10px 30px rgba(20, 70, 100, 0.18);
  }

  /* Front */
  .card-front {
    background:
      radial-gradient(circle at 92% 100%, var(--soft-panel) 0%, rgba(237,243,249,0) 38%),
      radial-gradient(circle at 22% 40%, var(--card-shade) 0%, var(--card-white) 55%);
  }
  .contact { position: absolute; left: 58px; top: 72px; }
  .person-name {
    font-weight: 700; font-size: 50px; line-height: 1.1; color: var(--brand-navy); letter-spacing: -0.5px;
  }
  .person-role {
    font-weight: 400; font-size: 36px; line-height: 1.2; color: var(--brand-sky); margin-top: 2px;
  }
  .phone {
    display: flex; align-items: center; gap: 12px;
    font-size: 32px; color: var(--brand-navy); margin-top: 12px;
  }
  .phone svg { width: 26px; height: 26px; }
  .address {
    position: absolute; left: 58px; bottom: 58px;
    display: flex; gap: 10px;
    font-style: normal;
    font-size: 31px; line-height: 1.18; color: var(--brand-navy);
  }
  .address svg { width: 20px; height: 28px; margin-top: 6px; flex: none; }

  .brand { position: absolute; display: flex; align-items: center; gap: 16px; }
  .brand-front { right: 60px; top: 58px; }
  .brand-dot {
    width: 100px; height: 100px; border-radius: 50%; flex: none;
    background: var(--brand-sky);
  }
  .brand-name {
    font-weight: 400; font-size: 66px; line-height: 1; color: var(--brand-navy);
  }
  .brand-tagline {
    font-weight: 400; font-size: 17px; letter-spacing: 0.5px; color: var(--brand-sky); margin-top: 6px;
  }

  /* Back */
  .card-back { background: var(--brand-blue); }
  .brand-back { left: 150px; top: 140px; }
  .brand-back .brand-dot { width: 116px; height: 116px; background: var(--field-white); }
  .brand-back .brand-name { color: var(--field-white); font-size: 76px; }
  .brand-back .brand-tagline { color: var(--field-white); font-size: 19px; }
  .appointment {
    position: absolute; left: 150px; right: 70px; bottom: 90px;
    display: flex; gap: 40px;
  }
  .appointment-field {
    flex: 1; display: flex; align-items: center; gap: 14px;
    color: var(--field-white); font-size: 24px;
  }
  .appointment-line { flex: 1; height: 44px; background: var(--field-white); }
</style>
</head>
<body>
<main class="sheet">
  <section class="card card-front" aria-label="Business card front">
    <div class="contact">
      <h1 class="person-name">Megan Dorrit</h1>
      <p class="person-role">Exercise Physiologist</p>
      <p class="phone">
        <svg viewBox="0 0 24 24" aria-hidden="true">
          <rect width="24" height="24" rx="4" fill="#4a9cd0"/>
          <path d="M8.2 5.5l2 2.6c.3.4.2.9-.1 1.2l-1 1c.7 1.6 1.9 2.8 3.5 3.5l1-1c.3-.3.8-.4 1.2-.1l2.6 2c.4.3.4.9.1 1.3l-1.1 1.2c-.6.6-1.5.8-2.3.5-3.5-1.3-6.2-4-7.5-7.5-.3-.8-.1-1.7.5-2.3L6.9 5.4c.4-.3 1-.3 1.3.1z" fill="#fff"/>
        </svg>
        0437 582 906
      </p>
    </div>

    <div class="brand brand-front">
      <div class="brand-dot" aria-hidden="true"></div>
      <div>
        <div class="brand-name">Vantora</div>
        <div class="brand-tagline">HEALTH &amp; REHABILITATION</div>
      </div>
    </div>

    <address class="address">
      <svg viewBox="0 0 20 28" aria-hidden="true">
        <path d="M10 0C4.5 0 0 4.4 0 9.8 0 17 10 28 10 28s10-11 10-18.2C20 4.4 15.5 0 10 0zm0 13.5a3.8 3.8 0 110-7.6 3.8 3.8 0 010 7.6z" fill="#4a9cd0"/>
      </svg>
      <span>14 Larkspur Bend Rd<br>Wexley South<br>(Gate 4, Brannock Fitness)</span>
    </address>
  </section>

  <section class="card card-back" aria-label="Business card back">
    <div class="brand brand-back">
      <div class="brand-dot" aria-hidden="true"></div>
      <div>
        <div class="brand-name">Vantora</div>
        <div class="brand-tagline">HEALTH &amp; REHABILITATION</div>
      </div>
    </div>
    <div class="appointment">
      <div class="appointment-field"><span>Date:</span><span class="appointment-line"></span></div>
      <div class="appointment-field"><span>Time:</span><span class="appointment-line"></span></div>
    </div>
  </section>
</main>
</body>
</html>
```